Mental Health

KVR HAVEN
Behavioral Health
4172 E. Dorrel St. Mesa, AZ 85217
Marguerite (480)555-0142 / Ivan 480-555-0187

Email: KVRHaven@Qortamail.com
Newly Remodeled & Spacious
g Staff
Registered Nurses
Licensed Independent &
Professional Substance &
Abuse Counselors
Behavioral Health Techs
Certified Caregivers
Behavioral Health &
Substance Abuse Professionals

To Refer a Patient
About Us
KVR Haven is a Fully Staffed Behavioral
Health Residential Facility, providing
treatment plans for adults suffering
with various Behavioral Health and
Substance Abuse disorders, while living
in a nice safe, clean and supportive
environment. Our home offers clients the
ability to learn the necessary skills to
help clients adapt, build self confidence
as well as independence, with the goal
of reducing the probability of a future
crisis or possible relapse. We offer
counseling programs, consisting of a
variety of addiction and recovery support
groups, independent living, coping and
social skills groups, as well as assisting
clients with using tools to create a resume
to help obtain employment and so much
more. We are committed to teaching
self management care and allowing
clients to understand how to utilize the
resources, skills and tools available for
long term success by providing superior
quality, all-inclusive living arrangements
and treatment options.

Thank you for your patience while I update the final content needed for us to make the final decision this week.

```html
<!DOCTYPE html>
<html lang="en">
<head>
<meta charset="utf-8">
<title>KVR Haven Business Cards</title>
<link rel="stylesheet" href="https://fonts.googleapis.com/css2?family=Marcellus&family=Montserrat:wght@500&family=Alegreya:wght@400&family=Roboto:wght@300;400;700&family=Noto+Serif:wght@700&display=swap">
<style>
  :root{
    --stage:#232323;
    --green:#84b735;
    --teal:#2a8a8c;
    --blue:#1466b1;
    --orange:#fb7033;
    --white:#ffffff;
    --ink:#1d1d1d;
  }
  *{box-sizing:border-box;margin:0;padding:0}
  html,body{width:1200px;height:1000px;overflow:hidden;background:var(--stage)}
  .stage{position:relative;width:1200px;height:1000px}
  .card{position:absolute;left:296px;width:608px;border-radius:24px;overflow:hidden}

  /* front card */
  .card--front{top:106px;height:368px;background:var(--white)}
  .front-field{position:absolute;left:0;top:0;width:100%;height:318px;
    background:linear-gradient(90deg,var(--green) 0%,var(--green) 30%,var(--teal) 62%,#1d6fa8 78%,var(--white) 78%)}
  .mark-circle{position:absolute;border-radius:50%;background:#f8f8f8}
  .card--front .mark-circle{left:292px;top:6px;width:320px;height:320px}
  .brand-row{position:absolute;left:30px;top:48px;display:flex;align-items:center;gap:8px}
  .brand-dot{width:44px;height:44px;border-radius:50%;background:var(--white)}
  .brand-rule{width:1.5px;height:46px;background:var(--white)}
  .brand-name{font-family:"Marcellus",serif;font-size:34px;line-height:1;color:var(--white);letter-spacing:0.5px;white-space:nowrap}
  .brand-tag{font-family:"Montserrat",sans-serif;font-weight:500;font-size:10px;letter-spacing:5.3px;color:var(--white);margin-top:3px;white-space:nowrap}
  .service-list{position:absolute;left:30px;top:126px;list-style:none;font-family:"Alegreya",serif;font-size:18px;color:var(--ink);line-height:26.5px}
  .service-list li{position:relative;padding-left:26px}
  .service-list li.bullet::before{content:"";position:absolute;left:2px;top:9px;width:11px;height:11px;border-radius:50%;background:var(--orange)}
  .location{position:absolute;left:29px;top:276px;font-family:"Roboto",sans-serif;font-size:15px;color:var(--ink)}
  .web-band{position:absolute;left:0;bottom:0;width:100%;height:50px;background:var(--orange);
    display:flex;align-items:center;justify-content:center;font-family:"Roboto",sans-serif;font-weight:700;font-size:15px;letter-spacing:6px;color:var(--white)}

  /* back card */
  .card--back{top:526px;height:366px;background:linear-gradient(90deg,var(--blue),var(--green));padding:5px}
  .back-inner{position:relative;width:100%;height:100%;background:var(--white);border-radius:19px;overflow:hidden}
  .back-band{position:absolute;left:0;top:117px;width:100%;height:208px;
    background:linear-gradient(90deg,var(--blue) 0%,#1f7aa6 40%,var(--teal) 62%,var(--green) 100%)}
  .card--back .mark-circle{left:295px;top:57px;width:288px;height:288px;background:var(--white)}
  .back-brand{position:absolute;left:26px;top:24px}
  .back-brand .brand-name{color:var(--blue);font-size:47px}
  .back-brand .brand-tag{color:var(--green);font-size:12.5px;letter-spacing:8px;margin-top:2px}
  .people{position:absolute;left:27px;top:137px;color:var(--white)}
  .people-name{font-family:"Noto Serif",serif;font-weight:700;font-size:25px}
  .people-role{font-family:"Roboto",sans-serif;font-weight:300;font-size:17px;margin-top:2px}
  .contact-list{position:absolute;left:27px;top:210px;list-style:none;font-family:"Roboto",sans-serif;font-weight:300;font-size:17px;color:var(--white);line-height:25.7px}
  .contact-list li{display:flex;align-items:center;gap:14px;white-space:nowrap}
  .contact-list svg{width:16px;height:16px;flex:none}
</style>
</head>
<body>
<div class="stage">

  <section class="card card--front">
    <div class="front-field"></div>
    <div class="mark-circle"></div>
    <div class="brand-row">
      <div class="brand-dot"></div>
      <div class="brand-rule"></div>
      <div>
        <div class="brand-name">KVR HAVEN</div>
        <div class="brand-tag">BEHAVIORAL HEALTH</div>
      </div>
    </div>
    <ul class="service-list">
      <li class="bullet">Residential Treatment Facility</li>
      <li class="bullet">Behavioral Health</li>
      <li>Professional / Techs</li>
      <li class="bullet">Registered Nurses</li>
      <li class="bullet">Behavioral Health Counseling</li>
    </ul>
    <div class="location">MERIDELL, AZ</div>
    <div class="web-band">www.KVR-Haven.com</div>
  </section>

  <section class="card card--back">
    <div class="back-inner">
      <div class="back-band"></div>
      <div class="mark-circle"></div>
      <div class="back-brand">
        <div class="brand-name">KVR HAVEN</div>
        <div class="brand-tag">BEHAVIORAL HEALTH</div>
      </div>
      <div class="people">
        <div class="people-name">Marguerite / Ivan</div>
        <div class="people-role">Administrators</div>
      </div>
      <ul class="contact-list">
        <li><svg viewBox="0 0 16 16"><path fill="#fb7033" d="M2 6c0-2 2-3 6-3s6 1 6 3v1h-3V5.5H5V7H2zM4 8l2-2h4l2 2 1 5H3z"/><circle cx="8" cy="10" r="1.6" fill="#1466b1"/></svg>(480) 555-0142 (Marguerite)</li>
        <li><svg viewBox="0 0 16 16"><path fill="#fb7033" d="M2 6c0-2 2-3 6-3s6 1 6 3v1h-3V5.5H5V7H2zM4 8l2-2h4l2 2 1 5H3z"/><circle cx="8" cy="10" r="1.6" fill="#1466b1"/></svg>(480) 555-0187 (Ivan)</li>
        <li><svg viewBox="0 0 16 16"><rect x="1" y="3" width="14" height="10" fill="#fb7033"/><path d="M1 3l7 6 7-6M1 13l5-5M15 13l-5-5" stroke="#1a6fa9" stroke-width="1.2" fill="none"/></svg>KVRHaven@Qortamail.com</li>
        <li><svg viewBox="0 0 16 16"><circle cx="8" cy="8" r="6.5" fill="none" stroke="#fb7033" stroke-width="1.5"/><ellipse cx="8" cy="8" rx="2.8" ry="6.5" fill="none" stroke="#fb7033" stroke-width="1.2"/><path d="M1.5 8h13M2.8 4.8h10.4M2.8 11.2h10.4" stroke="#fb7033" stroke-width="1.1"/></svg>www.KVR-Haven.com</li>
      </ul>
    </div>
  </section>

</div>
</body>
</html>
```